Fontenot Bayou Grillhouse (Owners Card)

Need a classy, but modern business card. I have included a promotional card for the steakhouse. I need one for myself (the owner) that is more professional.

Target Market(s)

General Public

Industry/Entity Type

Food service

Contact Information for Business Card

Name, business address, phone number, email, logo

Font styles to use
Serif
Sans Serif
Decorative
Script

Requirements
Must have
• My name (Darvel Pruitt), business address (327 Oakmere Street), phone number (510) 493-2615, email (Dpruittkr4@mailvane.example. On the back of the card: Psalms 27 1 The LORD is my light and my salvation— whom shall I fear? The LORD is the stronghold of my life— of whom shall I be afraid? 2 When the wicked advance against me to devour me, it is my enemies and my foes who will stumble and fall. 3 Though an army besiege me, my heart will not fear; though war break out against me, even then I will be confident.
Nice to have
• Something that’s bold, but modern and professional.

```html
<!DOCTYPE html>
<html lang="en">
<head>
<meta charset="utf-8">
<title>Fontenot Bayou Grillhouse — Owner Business Card</title>
<link href="https://fonts.googleapis.com/css2?family=Gelasio:wght@400;600&family=Tinos:wght@700&display=swap" rel="stylesheet">
<style>
  :root {
    --stage: #000000;
    --card-orange: #f47721;
    --card-white: #ffffff;
    --accent-lime: #b5cc2e;
    --brand-red: #d4432a;
    --ink-light: #ffffff;
  }
  * { margin: 0; padding: 0; box-sizing: border-box; }
  html, body {
    width: 1200px; height: 1200px; overflow: hidden;
    background: var(--stage);
  }
  .canvas { position: relative; width: 1200px; height: 1200px; }

  .card {
    position: absolute; left: 160px; width: 878px; height: 515px;
    box-shadow: 0 6px 18px rgba(0,0,0,0.6);
  }
  .card--front { top: 66px; display: flex; }
  .card--back {
    top: 618px; background: var(--card-orange);
    display: flex; flex-direction: column; align-items: center; justify-content: center;
    color: var(--ink-light); font-family: "Gelasio", Georgia, serif;
    font-size: 21px; line-height: 34px; text-align: center;
  }

  .front__brand {
    width: 451px; background: var(--card-white);
    display: flex; flex-direction: column; align-items: center; justify-content: center;
    gap: 14px;
  }
  .brand-dot { width: 58px; height: 58px; border-radius: 50%; background: var(--brand-red); }
  .brand-name {
    font-family: "Gelasio", Georgia, serif; font-weight: 600;
    color: var(--brand-red); font-size: 33px; line-height: 40px; text-align: center;
  }
  .front__stripe { width: 11px; background: var(--accent-lime); }
  .front__details {
    flex: 1; background: var(--card-orange); color: var(--ink-light);
    position: relative;
  }
  .owner-name {
    position: absolute; top: 153px; left: 0; right: 0; text-align: center;
    font-family: "Tinos", "Times New Roman", serif; font-weight: 700;
    font-size: 38px; letter-spacing: 0.5px;
  }
  .contact-list {
    position: absolute; top: 194px; right: 58px; list-style: none;
    font-family: "Gelasio", Georgia, serif; font-size: 20px;
  }
  .contact-list li {
    display: flex; align-items: center; justify-content: flex-end;
    gap: 16px; height: 34px;
  }
  .contact-icon { width: 16px; height: 16px; fill: var(--ink-light); flex: none; }

  .verse-title { margin-bottom: 34px; }
  .verse { width: 740px; margin-bottom: 34px; }
  .verse:last-child { margin-bottom: 0; }
</style>
</head>
<body>
<main class="canvas">
  <section class="card card--front">
    <div class="front__brand">
      <span class="brand-dot"></span>
      <div class="brand-name">Fontenot Bayou<br>Grillhouse</div>
    </div>
    <div class="front__stripe"></div>
    <div class="front__details">
      <h1 class="owner-name">DARVEL PRUITT</h1>
      <ul class="contact-list">
        <li>(510) 493-2615
          <svg class="contact-icon" viewBox="0 0 24 24"><path d="M6.6 10.8a15.1 15.1 0 0 0 6.6 6.6l2.2-2.2a1 1 0 0 1 1-.25 11.4 11.4 0 0 0 3.6.6 1 1 0 0 1 1 1V20a1 1 0 0 1-1 1A17 17 0 0 1 3 4a1 1 0 0 1 1-1h3.5a1 1 0 0 1 1 1c0 1.25.2 2.45.6 3.6a1 1 0 0 1-.25 1z"/></svg>
        </li>
        <li>Dpruittkr4@mailvane.example
          <svg class="contact-icon" viewBox="0 0 24 24"><path d="M7 1h10a2 2 0 0 1 2 2v18a2 2 0 0 1-2 2H7a2 2 0 0 1-2-2V3a2 2 0 0 1 2-2zm0 3v14h10V4zm5 15.5a1.2 1.2 0 1 0 0 2.4 1.2 1.2 0 0 0 0-2.4z"/></svg>
        </li>
        <li>327 Oakmere Street
          <svg class="contact-icon" viewBox="0 0 24 24"><path d="M12 1a7.5 7.5 0 0 0-7.5 7.5C4.5 14 12 23 12 23s7.5-9 7.5-14.5A7.5 7.5 0 0 0 12 1zm0 10.2a2.7 2.7 0 1 1 0-5.4 2.7 2.7 0 0 1 0 5.4z"/></svg>
        </li>
      </ul>
    </div>
  </section>

  <section class="card card--back">
    <p class="verse-title">Psalms 27</p>
    <p class="verse">The LORD is my light and my salvation— whom shall I fear? The LORD is the stronghold of my life— of whom shall I be afraid?</p>
    <p class="verse">When the wicked advance against me to devour me, it is my enemies and my foes who will stumble and fall.</p>
    <p class="verse">Though an army besiege me, my heart will not fear; though war break out against me, even then I will be confident.</p>
  </section>
</main>
</body>
</html>
```